TAVRO Capital Group LLC a High Risk Big Rewards company for Rich Young Entrepreneurs

We would like a very modern, powerful in the eyes of our customers, modern, minimalist feel, financial gain. this business card is for young Rich entrepreneurs who want to invest money into High Risk, Big Rewards Businesses. The card Should sell the business!! let your creativity go Wild! I pick most of the designers for this project because of your BOLD Designs, I would like this card to be Bold, Modern, Minimalist, use as many effects in your graphic Artist Mind, Do not let the Financial sound of this business to make you think Conservative that's the last thing we are! if you have a lot of money and you want to play a risky market call US
Updates

Project Deadline Extended
Reason: have not received, enough designs to choose 1st and second place, sure I have received over 100 designs but it seems most designers are submitting every card they have ever made before and calling it mine, please we are looking for fresh ideas please!

Target Market(s)

Private Risky Investors

Industry/Entity Type

Financial

Contact Information for Business Card

powerful in the eyes of our customers,modern, minimalist feel

Font styles to use
Other font styles liked:
• Modern feeling fonts

Requirements
Must have
• The Company Name is TAVRO Capital Group LLC and it must be on the CARD
• My Name, title, Cell , email
• Delvin Ashcroft G.E.D.
• Managing Member
• 555.038.6195
• delvin@tavrocapitalgroup.example
Nice to have
• try a black thick plastic card with round corners with Delvin Ashcroft GED (make sure GED is smaller than name) just on one side of the card, and my phone number with out the icons and email on the other side, this card should look like a exclusive credit card or exclusive VIP card, something you would never loose

```html
<!DOCTYPE html>
<html lang="en">
<head>
<meta charset="utf-8">
<title>TAVRO Capital Group LLC – Business Card</title>
<link rel="stylesheet" href="https://fonts.googleapis.com/css2?family=Open+Sans:wght@400;600;700&display=swap">
<style>
  :root {
    --backdrop: #e4e4e6;
    --card-black: #0b0b0b;
    --card-edge: #1c1c1c;
    --gold-light: #f6dc8a;
    --gold: #d4aa45;
    --gold-deep: #8e6a1f;
    --text-white: #f2f2f2;
    --ornament-tone: #3a3220;
    --illustration-tone: #6b5526;
  }
  * { box-sizing: border-box; margin: 0; padding: 0; }
  html, body {
    width: 1200px; height: 1200px; overflow: hidden;
    background: var(--backdrop);
    font-family: "Open Sans", Arial, sans-serif;
  }
  .canvas { position: relative; width: 1200px; height: 1200px; }

  .card {
    position: absolute; left: 220px;
    width: 760px; height: 440px;
    border-radius: 34px;
    background: linear-gradient(160deg, var(--card-edge) 0%, var(--card-black) 45%, #000 100%);
    overflow: hidden;
    box-shadow: 0 18px 40px rgba(0,0,0,0.28);
  }
  .card--front { top: 150px; }
  .card--back  { top: 640px; }

  .gold-rule {
    position: absolute; left: 0; right: 0; height: 5px;
    background: linear-gradient(90deg, var(--gold-deep), var(--gold-light) 30%, var(--gold) 60%, var(--gold-light) 85%, var(--gold-deep));
  }
  .gold-ring {
    position: absolute; width: 124px; height: 124px; border-radius: 50%;
    border: 7px solid var(--gold);
    box-shadow: inset 0 0 0 1px var(--gold-light), 0 0 0 1px var(--gold-deep);
  }
  .ornament {
    position: absolute; width: 190px; height: 160px;
    background: radial-gradient(ellipse at center, var(--ornament-tone) 0%, rgba(58,50,32,0.35) 50%, transparent 75%);
  }
  .illustration {
    position: absolute; left: 300px; top: 60px; width: 390px; height: 170px;
    border-radius: 20px;
    background: radial-gradient(ellipse at 50% 55%, var(--illustration-tone) 0%, #2a2110 55%, transparent 80%);
  }

  .company-name {
    position: absolute; left: 112px; top: 262px;
    color: var(--gold); font-weight: 700; font-size: 31px; letter-spacing: 2px;
  }
  .person-line {
    position: absolute; left: 112px; top: 310px;
    color: var(--text-white); font-size: 27px; font-weight: 400;
    display: flex; align-items: baseline; gap: 30px;
  }
  .person-name .credential { font-size: 17px; margin-left: 6px; }
  .person-title { font-size: 19px; }

  .contact-row {
    position: absolute; left: 40px; color: var(--text-white);
    display: flex; align-items: baseline;
  }
  .contact-label { width: 96px; font-size: 21px; }
  .contact-value { font-size: 25px; letter-spacing: 0.5px; }
</style>
</head>
<body>
<main class="canvas">

  <section class="card card--front" aria-label="Card front">
    <div class="ornament" style="left:-30px; top:-20px;" role="img" aria-label="Faint gold floral flourish in the top-left corner"></div>
    <div class="gold-ring" style="left:95px; top:70px;"></div>
    <div class="illustration" role="img" aria-label="Ornate gold and black decorated elephants illustration"></div>
    <div class="gold-rule" style="top:232px;"></div>
    <h1 class="company-name">TAVRO Capital Group LLC</h1>
    <p class="person-line">
      <span class="person-name">Delvin Ashcroft<span class="credential">GED</span></span>
      <span class="person-title">Managing Member</span>
    </p>
    <div class="gold-rule" style="top:372px;"></div>
  </section>

  <section class="card card--back" aria-label="Card back">
    <div class="gold-rule" style="top:36px;"></div>
    <p class="contact-row" style="top:72px;">
      <span class="contact-label">Call</span>
      <span class="contact-value">555.038.6195</span>
    </p>
    <p class="contact-row" style="top:118px;">
      <span class="contact-label">Email</span>
      <span class="contact-value">delvin@tavrocapitalgroup.example</span>
    </p>
    <div class="gold-rule" style="top:172px;"></div>
    <div class="gold-rule" style="top:206px;"></div>
    <div class="gold-ring" style="left:470px; top:250px;"></div>
    <div class="ornament" style="right:-30px; bottom:-20px;" role="img" aria-label="Faint gold floral flourish in the bottom-right corner"></div>
  </section>

</main>
</body>
</html>
```